church business card design

we have a logo and would like our business card to complement the logo. we would prefer the logo in white on a coloured background - probably blue. Under the logo or near it we would have the Words 'Welcome All. Serve Well. Walk in Faith.'
We would like some yellow/gold highlights. We like the design by marlow inkworks 88 front of card - https://www.pitchvelta.com/businesscard-design/contest/5182094

Our church is multicultural, inner city, friendly, warm welcoming and that's the feel we would like. there's also an element of being spontaneous, so a swirl or swoosh might help give that feel. the example card above had some curved shapes on the front of the card for example.
on the second side of the card would have the details of the Senior Pastor and the contact details for the church.
after the business card we would be looking at letterhead and an A5 flyer for printing but also as document templates so we can create invitations etc going forward

```html
<!DOCTYPE html>
<html lang="en">
<head>
<meta charset="utf-8">
<title>Harbor Light Church – Stationery</title>
<link href="https://fonts.googleapis.com/css2?family=Poppins:wght@400;500;600;700&display=swap" rel="stylesheet">
<style>
  :root{
    --backdrop:#d0d0d0;
    --navy:#1f2a56;
    --royal:#0a4a9c;
    --royal-mid:#164a98;
    --gold:#c9a23a;
    --gold-light:#fbe7a1;
    --gold-deep:#a8781c;
    --paper:#ffffff;
    --hill:#c9c8cb;
    --white:#ffffff;
  }
  *{box-sizing:border-box;margin:0;padding:0}
  html,body{width:1200px;height:1170px;overflow:hidden;background:var(--backdrop);font-family:"Poppins",sans-serif;color:var(--white)}
  .stage{position:relative;width:1200px;height:1170px}

  .brand{position:absolute;text-align:center;line-height:1}
  .brand-name{font-weight:600;color:var(--white);letter-spacing:.4px;display:flex;align-items:center;justify-content:center;gap:6px;white-space:nowrap}
  .brand-dot{display:inline-block;border-radius:50%;background:var(--white);flex:none}
  .brand-tagline{font-weight:700;text-transform:uppercase;display:flex;align-items:center;justify-content:center;gap:4px;margin-top:7px;white-space:nowrap}
  .brand-tagline::before,.brand-tagline::after{content:"";display:block;height:1.5px;background:var(--white)}

  /* Letterhead */
  .letterhead{position:absolute;left:148px;top:155px;width:601px;height:845px;background:var(--paper);overflow:hidden}
  .letterhead-header{position:absolute;left:0;top:0}
  .letterhead .brand{left:0;right:0;top:40px}
  .letterhead .brand-name{font-size:24px}
  .letterhead .brand-dot{width:9px;height:9px}
  .letterhead .brand-tagline{font-size:5.5px;margin-top:9px}
  .letterhead .brand-tagline::before,.letterhead .brand-tagline::after{width:11px}
  .letterhead-landscape{position:absolute;left:0;top:772px;width:601px;height:32px;
    background:linear-gradient(to bottom,rgba(201,200,203,.2) 0%,var(--hill) 45%,var(--hill) 100%)}
  .letterhead-rule{position:absolute;left:0;top:804px;width:601px;height:2px;background:var(--paper)}
  .letterhead-footer{position:absolute;left:0;top:806px;width:601px;height:39px;
    background:linear-gradient(90deg,var(--navy) 0%,var(--royal-mid) 40%,var(--royal) 70%,var(--navy) 100%)}
  .contact{position:absolute;top:0;height:39px;display:flex;align-items:center;gap:6px;font-size:13px;letter-spacing:.4px;white-space:nowrap}
  .contact-icon{width:15px;height:15px;flex:none}

  /* Business cards */
  .card{position:absolute;overflow:hidden}
  .card-front{left:798px;top:586px;width:323px;height:183px}
  .card-back{left:798px;top:817px;width:327px;height:186px}
  .card-art{position:absolute;left:0;top:0}
  .card-front .brand{left:0;right:0;top:66px}
  .card-front .brand-name{font-size:20px}
  .card-front .brand-dot{width:8px;height:8px}
  .card-front .brand-tagline{font-size:5px;margin-top:8px}
  .card-front .brand-tagline::before,.card-front .brand-tagline::after{width:10px}
  .card-back .brand{left:21px;top:30px;text-align:left}
  .card-back .brand-name{font-size:15px;justify-content:flex-start;gap:5px}
  .card-back .brand-dot{width:6px;height:6px}
  .card-back .brand-tagline{font-size:4.5px;justify-content:flex-start;margin-top:7px}
  .card-back .brand-tagline::before,.card-back .brand-tagline::after{width:9px}

  .card-detail{position:absolute;display:flex;align-items:center;gap:5px;font-size:9px;letter-spacing:.3px;white-space:nowrap}
  .card-detail .contact-icon{width:17px;height:17px}
  .person-name{font-weight:700;font-size:8.5px;text-transform:uppercase;letter-spacing:.3px;line-height:1.1}
  .person-role{font-size:4.5px;line-height:1.2}
</style>
</head>
<body>
<div class="stage">

  <section class="letterhead" aria-label="Letterhead">
    <svg class="letterhead-header" width="601" height="160" viewBox="0 0 601 160" aria-hidden="true">
      <defs>
        <linearGradient id="lh-blue" x1="0" y1="0" x2="1" y2="0">
          <stop offset="0" stop-color="#0d4596"/>
          <stop offset=".4" stop-color="#0a4a9c"/>
          <stop offset=".6" stop-color="#163f8c"/>
          <stop offset=".8" stop-color="#1f2a56"/>
          <stop offset="1" stop-color="#1f2a56"/>
        </linearGradient>
        <linearGradient id="lh-gold" x1="0" y1="0" x2="1" y2="0">
          <stop offset="0" stop-color="#c9a23a"/>
          <stop offset=".25" stop-color="#fbe7a1"/>
          <stop offset=".5" stop-color="#d9b153"/>
          <stop offset=".8" stop-color="#c9a23a"/>
          <stop offset="1" stop-color="#a8781c"/>
        </linearGradient>
      </defs>
      <path d="M0 0H601V130C460 98 300 92 150 118 90 128 40 142 0 155Z" fill="url(#lh-blue)"/>
      <path d="M0 134C150 96 320 80 450 92 510 98 560 108 585 122 520 108 430 98 330 98 210 100 90 122 0 150Z" fill="url(#lh-gold)"/>
      <path d="M0 150C90 122 210 100 330 98 430 98 520 108 585 122L601 126V132C460 102 300 96 150 120 90 130 40 144 0 157Z" fill="#123d86"/>
    </svg>
    <div class="brand">
      <div class="brand-name"><span class="brand-dot"></span>Harbor Light Church</div>
      <div class="brand-tagline">Welcome All. Serve Well. Walk in Faith</div>
    </div>

    <div class="letterhead-landscape" role="img" aria-label="Silhouette of rolling hills with a cross on a hilltop"></div>
    <div class="letterhead-rule"></div>

    <footer class="letterhead-footer">
      <div class="contact" style="left:48px">
        <svg class="contact-icon" viewBox="0 0 16 16" aria-hidden="true"><circle cx="8" cy="8" r="8" fill="var(--gold)"/><path d="M5.3 4.2l1.4 1.7-.8 1c.6 1.2 1.4 2 2.6 2.6l1-.8 1.7 1.4-.9 1.3C7.6 11.2 4.8 8.4 4 5.1z" fill="var(--navy)"/></svg>
        123-456-7890
      </div>
      <div class="contact" style="left:228px">
        <svg class="contact-icon" viewBox="0 0 16 16" aria-hidden="true"><circle cx="8" cy="8" r="8" fill="var(--gold)"/><rect x="4.2" y="5.2" width="7.6" height="5.6" fill="none" stroke="var(--navy)" stroke-width="1"/><path d="M4.2 5.2L8 8.4l3.8-3.2" fill="none" stroke="var(--navy)" stroke-width="1"/></svg>
        loremipsum@com
      </div>
      <div class="contact" style="left:428px">
        <svg class="contact-icon" viewBox="0 0 16 16" aria-hidden="true"><circle cx="8" cy="8" r="8" fill="var(--gold)"/><circle cx="8" cy="8" r="4" fill="none" stroke="var(--navy)" stroke-width="1"/><ellipse cx="8" cy="8" rx="1.7" ry="4" fill="none" stroke="var(--navy)" stroke-width=".9"/><path d="M4 8h8" stroke="var(--navy)" stroke-width=".9"/></svg>
        loremipsum.com
      </div>
    </footer>
  </section>

  <section class="card card-front" aria-label="Business card front">
    <svg class="card-art" width="323" height="183" viewBox="0 0 323 183" aria-hidden="true">
      <defs>
        <linearGradient id="cf-blue" x1="0" y1="0" x2="0" y2="1">
          <stop offset="0" stop-color="#1f2a56"/>
          <stop offset=".45" stop-color="#0b4a9e"/>
          <stop offset=".8" stop-color="#1f2a56"/>
          <stop offset="1" stop-color="#1f2a56"/>
        </linearGradient>
        <linearGradient id="card-gold" x1="0" y1="0" x2="1" y2="0">
          <stop offset="0" stop-color="#d9b153"/>
          <stop offset=".2" stop-color="#fbe7a1"/>
          <stop offset=".45" stop-color="#e3c06a"/>
          <stop offset=".7" stop-color="#fbe7a1"/>
          <stop offset=".85" stop-color="#c9a23a"/>
          <stop offset="1" stop-color="#a8781c"/>
        </linearGradient>
      </defs>
      <rect width="323" height="183" fill="url(#cf-blue)"/>
      <path d="M0 24C90 4 230 4 323 32 230 14 100 12 0 34Z" fill="#2a3f7e" opacity=".55"/>
      <path d="M0 150C110 178 230 168 323 140V145C230 172 110 180 0 156Z" fill="url(#card-gold)"/>
      <path d="M0 162C110 180 230 170 323 150V183H0Z" fill="url(#card-gold)"/>
    </svg>
    <div class="brand">
      <div class="brand-name"><span class="brand-dot"></span>Harbor Light Church</div>
      <div class="brand-tagline">Welcome All. Serve Well. Walk in Faith</div>
    </div>
  </section>

  <section class="card card-back" aria-label="Business card back">
    <svg class="card-art" width="327" height="186" viewBox="0 0 327 186" aria-hidden="true">
      <defs>
        <linearGradient id="cb-blue" x1="0" y1="0" x2="0" y2="1">
          <stop offset="0" stop-color="#1f2a56"/>
          <stop offset=".5" stop-color="#0b4a9e"/>
          <stop offset=".8" stop-color="#1f2a56"/>
          <stop offset="1" stop-color="#1f2a56"/>
        </linearGradient>
      </defs>
      <rect width="327" height="186" fill="url(#cb-blue)"/>
      <path d="M0 150C110 176 230 166 327 138V143C230 170 110 178 0 156Z" fill="url(#card-gold)"/>
      <path d="M0 160C110 180 230 170 327 150V186H0Z" fill="url(#card-gold)"/>
    </svg>
    <div class="brand">
      <div class="brand-name"><span class="brand-dot"></span>Harbor Light Church</div>
      <div class="brand-tagline">Welcome All. Serve Well. Walk in Faith</div>
    </div>

    <div class="card-detail" style="left:22px;top:104px">
      <svg class="contact-icon" viewBox="0 0 18 18" aria-hidden="true"><circle cx="9" cy="9" r="8.2" fill="none" stroke="#fff" stroke-width="1"/><circle cx="9" cy="9" r="6.4" fill="#fff"/><circle cx="9" cy="7.4" r="1.8" fill="var(--royal)"/><path d="M5.8 12.4c.5-2 1.7-2.8 3.2-2.8s2.7.8 3.2 2.8z" fill="var(--royal)"/></svg>
      <div><div class="person-name">Lorem Ipsum Text</div><div class="person-role">Lorem ipsum text</div></div>
    </div>
    <div class="card-detail" style="left:22px;top:128px">
      <svg class="contact-icon" viewBox="0 0 18 18" aria-hidden="true"><circle cx="9" cy="9" r="8.2" fill="none" stroke="#fff" stroke-width="1"/><circle cx="9" cy="9" r="6.4" fill="#fff"/><path d="M6.3 5.2l1.4 1.7-.8 1c.6 1.2 1.4 2 2.6 2.6l1-.8 1.7 1.4-.9 1.3C8.6 12.2 5.8 9.4 5 6.1z" fill="var(--royal)"/></svg>
      123-456-7890
    </div>
    <div class="card-detail" style="left:173px;top:104px">
      <svg class="contact-icon" viewBox="0 0 18 18" aria-hidden="true"><circle cx="9" cy="9" r="8.2" fill="none" stroke="#fff" stroke-width="1"/><circle cx="9" cy="9" r="6.4" fill="#fff"/><circle cx="9" cy="9" r="3.8" fill="none" stroke="var(--royal)" stroke-width=".9"/><ellipse cx="9" cy="9" rx="1.6" ry="3.8" fill="none" stroke="var(--royal)" stroke-width=".8"/><path d="M5.2 9h7.6" stroke="var(--royal)" stroke-width=".8"/></svg>
      loremipsum.com
    </div>
    <div class="card-detail" style="left:173px;top:126px">
      <svg class="contact-icon" viewBox="0 0 18 18" aria-hidden="true"><circle cx="9" cy="9" r="8.2" fill="none" stroke="#fff" stroke-width="1"/><circle cx="9" cy="9" r="6.4" fill="#fff"/><rect x="5.6" y="6.6" width="6.8" height="4.8" fill="none" stroke="var(--royal)" stroke-width=".9"/><path d="M5.6 6.6L9 9.4l3.4-2.8" fill="none" stroke="var(--royal)" stroke-width=".9"/></svg>
      loremipsum@com
    </div>
  </section>

</div>
</body>
</html>
```